Business Card Re-design

We are looking for a fresh bold look for general office business cards. We are a staffing agency that staffs industrial, coal mining, and clerical jobs.
Tag Line: We pair the RIGHT workers with the RIGHT shifts.
Marrowdale Office: 437 W. Hollowmere Ave, Marrowdale, OH - 47298
p. 812.555.0183 f. 812.555.0196
Fenwick Ridge Office: 926 S. Larkfen Way, Fenwick Ridge, OH - 47231
p. 812.555.0127 f. 812.555.0196
Absentee/Emergency 24hr Hotline 812.555.0164 opt.1
www.tallowcrestworkforce.example

```html
<!DOCTYPE html>
<html lang="en">
<head>
<meta charset="utf-8">
<title>Tallowcrest Workforce — Business Card</title>
<link href="https://fonts.googleapis.com/css2?family=Montserrat:ital,wght@0,400;0,500;0,600;0,700;1,700&display=swap" rel="stylesheet">
<style>
  :root {
    --backdrop: #2e8534;
    --navy: #2f4776;
    --ink: #1f3d6b;
    --leaf: #5aac44;
    --paper: #ffffff;
  }
  * { margin: 0; padding: 0; box-sizing: border-box; }
  html, body { width: 1200px; height: 1000px; overflow: hidden; }
  body {
    background: var(--backdrop);
    font-family: "Montserrat", Arial, sans-serif;
    position: relative;
  }
  .card {
    position: absolute;
    left: 236px;
    width: 727px;
    height: 416px;
    border-radius: 22px;
    overflow: hidden;
    box-shadow: 0 14px 30px rgba(0, 0, 0, 0.28);
  }
  /* Front */
  .card-front { top: 53px; background: var(--navy); color: var(--paper); }
  .front-brand {
    position: absolute;
    top: 146px; left: 0; right: 0;
    text-align: center;
    font-size: 44px;
    font-weight: 700;
    letter-spacing: 1px;
    line-height: 1.05;
    color: var(--paper);
    text-transform: uppercase;
  }
  .tagline {
    position: absolute;
    top: 267px; left: 0; right: 0;
    text-align: center;
    font-size: 16px;
    font-weight: 500;
    letter-spacing: 0.7px;
    text-transform: uppercase;
  }
  .tagline em { color: var(--leaf); font-weight: 700; }

  /* Back */
  .card-back { top: 529px; background: var(--paper); color: var(--ink); }
  .back-brand {
    position: absolute;
    top: 28px; left: 44px;
    display: flex; align-items: center; gap: 10px;
    font-size: 21px; font-weight: 700; line-height: 1.1;
    color: var(--ink);
    text-transform: uppercase;
  }
  .back-brand .mark { width: 14px; height: 14px; background: var(--leaf); }
  .hotline {
    position: absolute;
    top: 0; right: 0;
    width: 381px; height: 96px;
    background: var(--navy);
    border-bottom-left-radius: 22px;
    text-align: right;
    padding: 31px 34px 0 0;
  }
  .hotline-title { color: var(--leaf); font-size: 14.5px; font-weight: 600; letter-spacing: 0.3px; text-transform: uppercase; }
  .hotline-number { color: var(--paper); font-size: 16px; font-weight: 500; margin-top: 5px; display: flex; justify-content: flex-end; align-items: center; gap: 5px; }
  .office { position: absolute; top: 166px; font-size: 16.5px; font-weight: 500; }
  .office-west { left: 42px; }
  .office-east { right: 37px; text-align: right; }
  .office-name { color: var(--leaf); font-size: 22px; font-weight: 600; letter-spacing: 0.8px; margin-bottom: 10px; text-transform: uppercase; }
  .line { display: flex; align-items: flex-start; gap: 10px; line-height: 21px; margin-bottom: 8px; }
  .office-east .line { justify-content: flex-end; }
  .line svg { flex: none; margin-top: 3px; }
  .footer {
    position: absolute; left: 0; right: 0; bottom: 0;
    height: 63px; background: var(--navy);
    color: var(--paper); font-size: 16.5px; font-weight: 500; letter-spacing: 0.3px;
    display: flex; align-items: center; justify-content: center;
  }
</style>
</head>
<body>
  <section class="card card-front">
    <div class="front-brand">Tallowcrest<br>Workforce</div>
    <p class="tagline">We pair the <em>right</em> workers with the <em>right</em> shifts</p>
  </section>

  <section class="card card-back">
    <div class="back-brand"><span class="mark"></span><span>Tallowcrest<br>Workforce</span></div>

    <div class="hotline">
      <p class="hotline-title">Absentee/Emergency 24hr Hotline</p>
      <p class="hotline-number">
        <svg width="14" height="14" viewBox="0 0 24 24" fill="#ffffff"><path d="M6.6 10.8a15.1 15.1 0 0 0 6.6 6.6l2.2-2.2a1 1 0 0 1 1-.25 11.4 11.4 0 0 0 3.6.57 1 1 0 0 1 1 1V20a1 1 0 0 1-1 1A17 17 0 0 1 3 4a1 1 0 0 1 1-1h3.5a1 1 0 0 1 1 1 11.4 11.4 0 0 0 .57 3.6 1 1 0 0 1-.25 1z"/></svg>
        812.555.0164 (opt.1)
      </p>
    </div>

    <div class="office office-west">
      <h2 class="office-name">Marrowdale</h2>
      <p class="line">
        <svg width="16" height="16" viewBox="0 0 24 24" fill="#5aac44"><path d="M6.6 10.8a15.1 15.1 0 0 0 6.6 6.6l2.2-2.2a1 1 0 0 1 1-.25 11.4 11.4 0 0 0 3.6.57 1 1 0 0 1 1 1V20a1 1 0 0 1-1 1A17 17 0 0 1 3 4a1 1 0 0 1 1-1h3.5a1 1 0 0 1 1 1 11.4 11.4 0 0 0 .57 3.6 1 1 0 0 1-.25 1z"/></svg>
        812.555.0183
      </p>
      <p class="line">
        <svg width="18" height="16" viewBox="0 0 24 20" fill="#5aac44"><rect x="0" y="5" width="5" height="15" rx="1"/><rect x="6" y="0" width="13" height="6"/><rect x="6" y="7" width="18" height="13" rx="1"/><rect x="9" y="10" width="2.5" height="2.5" fill="#fff"/><rect x="13" y="10" width="2.5" height="2.5" fill="#fff"/><rect x="9" y="14" width="2.5" height="2.5" fill="#fff"/><rect x="13" y="14" width="2.5" height="2.5" fill="#fff"/></svg>
        812.555.0196
      </p>
      <p class="line">
        <svg width="16" height="18" viewBox="0 0 24 28" fill="#5aac44"><path d="M12 0a10 10 0 0 0-10 10c0 7.5 10 18 10 18s10-10.5 10-18A10 10 0 0 0 12 0zm0 14a4 4 0 1 1 0-8 4 4 0 0 1 0 8z"/></svg>
        <span>437 W. Hollowmere Ave,<br>Marrowdale, OH - 47298</span>
      </p>
    </div>

    <div class="office office-east">
      <h2 class="office-name">Fenwick Ridge</h2>
      <p class="line">
        812.555.0127
        <svg width="16" height="16" viewBox="0 0 24 24" fill="#5aac44"><path d="M6.6 10.8a15.1 15.1 0 0 0 6.6 6.6l2.2-2.2a1 1 0 0 1 1-.25 11.4 11.4 0 0 0 3.6.57 1 1 0 0 1 1 1V20a1 1 0 0 1-1 1A17 17 0 0 1 3 4a1 1 0 0 1 1-1h3.5a1 1 0 0 1 1 1 11.4 11.4 0 0 0 .57 3.6 1 1 0 0 1-.25 1z"/></svg>
      </p>
      <p class="line">
        812.555.0196
        <svg width="18" height="16" viewBox="0 0 24 20" fill="#5aac44"><rect x="0" y="5" width="5" height="15" rx="1"/><rect x="6" y="0" width="13" height="6"/><rect x="6" y="7" width="18" height="13" rx="1"/><rect x="9" y="10" width="2.5" height="2.5" fill="#fff"/><rect x="13" y="10" width="2.5" height="2.5" fill="#fff"/><rect x="9" y="14" width="2.5" height="2.5" fill="#fff"/><rect x="13" y="14" width="2.5" height="2.5" fill="#fff"/></svg>
      </p>
      <p class="line">
        <span>926 S. Larkfen Way,<br>Fenwick Ridge, OH - 47231</span>
        <svg width="16" height="18" viewBox="0 0 24 28" fill="#5aac44"><path d="M12 0a10 10 0 0 0-10 10c0 7.5 10 18 10 18s10-10.5 10-18A10 10 0 0 0 12 0zm0 14a4 4 0 1 1 0-8 4 4 0 0 1 0 8z"/></svg>
      </p>
    </div>

    <div class="footer">www.tallowcrestworkforce.example</div>
  </section>
</body>
</html>
```